Business card for Chicago based Private Equity Company

We need a business card for our PE company called Crestline Partners. We want a simple and clean, yet creative card design. The back side should reflect our logo. Also would like to see embossed ideas. Should reflect strength and growth. Our logo is attached. Also need editable file. Details are as follows for Business Card:

Dale Moravec Co-Founder 2750 Larkin Avenue Suite 410 Oak Brook, IL 60587 http://www.crestlinepartnersllc.example (D) 630.555.0142 (C) 312.555.0178 (E) dm@crestlinepartnersllc.example

```html
<!DOCTYPE html>
<html lang="en">
<head>
<meta charset="utf-8">
<title>Crestline Partners – Business Card</title>
<link rel="stylesheet" href="https://fonts.googleapis.com/css2?family=Lato:wght@400;700&display=swap">
<style>
  :root {
    --ink: #0b0b0b;
    --paper: #ffffff;
    --backdrop: #3a3a3a;
    --muted: #222222;
  }
  * { margin: 0; padding: 0; box-sizing: border-box; }
  html, body {
    width: 1200px; height: 926px; overflow: hidden;
    background: var(--backdrop);
    font-family: "Lato", Arial, sans-serif;
  }
  .stage {
    position: relative; width: 1200px; height: 926px;
  }
  .card {
    position: absolute; left: 240px;
    width: 720px; height: 411px;
    overflow: hidden;
    box-shadow: 0 10px 30px rgba(0,0,0,0.45);
  }
  .card--front { top: 40px; background: var(--paper); color: var(--ink); }
  .card--back { top: 475px; background: var(--ink); color: var(--paper); }

  .brand { display: flex; align-items: center; gap: 10px; }
  .brand__dot {
    width: 34px; height: 34px; border-radius: 50%;
    border: 4px solid currentColor;
  }
  .brand__name {
    font-weight: 400; letter-spacing: 0.14em; text-transform: uppercase;
    line-height: 1;
  }
  .card--front .brand { position: absolute; left: 38px; top: 36px; }
  .card--front .brand__name { font-size: 17px; }

  .card--back .brand {
    position: absolute; left: 50%; top: 50%;
    transform: translate(-50%, -50%); gap: 18px;
  }
  .card--back .brand__dot { width: 70px; height: 70px; border-width: 8px; }
  .card--back .brand__name { font-size: 34px; }

  .contact { position: absolute; left: 40px; top: 128px; }
  .contact__name { font-size: 27px; font-weight: 400; }
  .contact__name strong { font-weight: 700; }
  .contact__role { font-size: 15px; margin-top: 2px; color: var(--muted); }
  .contact__lines { list-style: none; margin-top: 18px; font-size: 16px; line-height: 1.35; color: var(--muted); }

  .emblem {
    position: absolute; right: -70px; top: 40px;
    width: 330px; height: 330px;
  }
  .address-band {
    position: absolute; left: 0; right: 0; bottom: 0; height: 62px;
    background: var(--ink); color: var(--paper);
    display: flex; align-items: center; padding-left: 40px;
    font-size: 18px; letter-spacing: 0.12em;
  }
</style>
</head>
<body>
<main class="stage">
  <section class="card card--front" aria-label="Business card front">
    <div class="brand">
      <span class="brand__dot"></span>
      <span class="brand__name">Crestline Partners</span>
    </div>
    <div class="contact">
      <h1 class="contact__name">Dale <strong>Moravec</strong></h1>
      <p class="contact__role">Co-Founder</p>
      <ul class="contact__lines">
        <li>(D) 630.555.0142</li>
        <li>(C) 312.555.0178</li>
        <li>(E) dm@crestlinepartnersllc.example</li>
        <li>http://www.crestlinepartnersllc.example</li>
      </ul>
    </div>
    <svg class="emblem" viewBox="0 0 330 330" aria-hidden="true">
      <circle cx="165" cy="165" r="150" fill="none" stroke="var(--ink)" stroke-width="22"/>
    </svg>
    <div class="address-band">2750 Larkin Avenue Suite 410 Oak Brook, IL 60587</div>
  </section>

  <section class="card card--back" aria-label="Business card back">
    <div class="brand">
      <span class="brand__dot"></span>
      <span class="brand__name">Crestline Partners</span>
    </div>
  </section>
</main>
</body>
</html>
```